Dinewell - Tablet App Design Project

I have a Tablet app that serves as a restaurant reservation system. The design that i currently have is very basic apple design. I am looking for it to have a much more professional appeal.

Please review the attached document which contains all of the screen shots for the app.
Updates

This Project has now been Guaranteed.  I look forward to reviewing your designs.

Brent

Reason: I am extending my deadline because i just changed this contest to guaranteed and have received a ton more "acceptances" because of it and I want to give those designers a chance to submit a design.

Target Market(s)

restaurant owners

Industry/Entity Type

Restaurant

Requirements
Must have
• On the seating chart i am changing the feature that shows the tables highlighted and instead would like that replace with a badge. So the list of wait staff across the top of the seating chart would instead have a number next to their name and would correspond with the badge on the table to determine their section.

So for example:
Ada would have a number 1 in front of her name and tables 18, 19, 20, and 31 would have a little badge in the upper right hand corner with the number "1" inside the badge.
Uma would have a number 2 in front of her name and tables 6, 7, and 11 would have a little badge in the upper right hand corner with the number " 2" inside the badge.
Nora would have a number 3 in front of her name and tables 12, 13, 27, 28, 29, and 30 would have a little badge in the upper right hand corner with the number " 3" inside the badge.

The names on the top will all be ONE color

Also, i would like an icon developed to replace the "C" you see next to some of the people's name in the reservation and waitlist slots. Also, i would like a better looking "check mark".

```html
<!DOCTYPE html>
<html lang="en">
<head>
<meta charset="utf-8">
<title>Dinewell – Host Stand</title>
<link href="https://fonts.googleapis.com/css2?family=Arimo:ital,wght@0,400;0,700;1,400&display=swap" rel="stylesheet">
<style>
:root{
  --status-bg:#1c1f24;
  --topbar-top:#dfe6ee;
  --topbar-bottom:#a9b8c8;
  --green-top:#5fae3c;
  --green-bottom:#2f7a1c;
  --cyan-top:#8ee3f2;
  --cyan-bottom:#41bcd6;
  --stats-bg:#d9dadc;
  --stat-top:#fbfbfb;
  --stat-bottom:#e3e3e3;
  --stage:#2f3a4b;
  --stage-dark:#263041;
  --panel:#d6d7d9;
  --panel-edge:#b9babd;
  --ink:#111;
  --ink-soft:#555;
  --ink-faded:#8a8a8a;
  --line:#c9c9c9;
  --tick:#4caf2a;
  --bubble:#3d86c9;
  --wait-green:#3b9a1e;
}
*{box-sizing:border-box;margin:0;padding:0}
html,body{width:1200px;height:900px;overflow:hidden}
body{font-family:"Arimo",Arial,sans-serif;color:var(--ink);
  background:radial-gradient(ellipse at 60% 40%,var(--stage) 0%,var(--stage-dark) 100%);position:relative}
.status-bar{position:absolute;left:0;top:0;width:1200px;height:22px;background:var(--status-bg);
  color:#fff;font-size:14px;font-weight:700;display:flex;align-items:center;justify-content:space-between;padding:0 8px}
.status-bar .clock{position:absolute;left:0;right:0;text-align:center;pointer-events:none}
.top-bar{position:absolute;left:0;top:22px;width:1200px;height:68px;
  background:linear-gradient(var(--topbar-top),var(--topbar-bottom));border-bottom:1px solid #7d8ea0}
.nav-btn{position:absolute;top:18px;height:38px;border-radius:5px;color:#fff;font-size:17px;
  display:flex;align-items:center;justify-content:center;border:1px solid #1f5a10;
  background:linear-gradient(var(--green-top),var(--green-bottom));box-shadow:inset 0 1px 0 rgba(255,255,255,.35),0 1px 2px rgba(0,0,0,.35)}
.nav-btn.is-active{background:linear-gradient(var(--cyan-top),var(--cyan-bottom));border-color:#2b8ea5}
.app-title{position:absolute;left:0;right:0;top:2px;text-align:center;color:#fff;font-size:56px;
  text-shadow:0 2px 3px rgba(0,0,0,.45)}
.stats-bar{position:absolute;left:0;top:90px;width:1200px;height:73px;background:var(--stats-bg);border-bottom:1px solid #999}
.stat{position:absolute;top:7px;height:57px;border:1px solid #8d8d8d;border-radius:5px;
  background:linear-gradient(var(--stat-top),var(--stat-bottom));text-align:center;
  display:flex;flex-direction:column;justify-content:center;font-size:17px;line-height:1.3}
.stat .label{font-weight:700}
.stat.now{font-weight:700;font-size:18px}
.stat.soft .label{font-weight:400}
.wait-list{position:absolute;left:17px;top:188px;width:370px;height:670px;background:var(--panel);
  border:1px solid var(--panel-edge);border-radius:4px;box-shadow:0 2px 4px rgba(0,0,0,.4)}
.wait-head{height:32px;background:linear-gradient(var(--green-top),var(--green-bottom));border-radius:4px 4px 0 0;
  color:#fff;font-size:19px;display:flex;align-items:center;gap:8px;padding-left:10px}
.wait-input{margin:10px 11px 0;height:35px;border:1px solid #999;background:#fff;font-style:italic;
  color:#999;font-size:14px;display:flex;align-items:center;padding-left:8px}
.wait-rows{margin:10px 11px 0;height:570px;background:#fff;border:1px solid #999;list-style:none}
.wait-row{height:57px;border-bottom:1px solid #e2e2e2;display:flex;justify-content:space-between;padding:10px 10px 0}
.wait-row .name{font-size:16px}
.wait-row .party{font-size:13px;font-style:italic}
.wait-row .since{font-size:14px;padding-top:3px}
.wait-row .since.recent{color:var(--wait-green)}
.res-card{position:absolute;width:370px;background:var(--panel);border:1px solid var(--panel-edge);
  border-radius:4px;padding:0 6px 6px;box-shadow:0 2px 4px rgba(0,0,0,.4)}
.card-head{height:31px;display:flex;align-items:center;font-size:13px}
.card-head .time{margin-left:6px;width:148px}
.card-head .fill{margin-left:5px;width:96px;color:#222}
.card-head .fill.full{color:var(--wait-green)}
.card-head .size{margin-left:4px;width:58px}
.card-body{background:#fff;border:1px solid #888}
.res-row{height:42px;display:flex;border-bottom:1px solid #eee}
.res-row:last-child{border-bottom:0}
.guest{flex:1;padding:6px 0 0 10px;font-size:13px}
.guest .note{font-size:10px;font-style:italic;margin-top:2px}
.res-row.faded .guest,.res-row.faded .count,.res-row.faded .total{color:var(--ink-faded)}
.flags{width:62px;display:flex;align-items:center;justify-content:flex-end;gap:4px}
.count{width:46px;display:flex;align-items:center;justify-content:center;font-size:14px;font-weight:700}
.res-row.faded .count{font-weight:400;font-size:12px}
.total{width:43px;border-left:1px solid #888;font-size:12px;color:var(--ink-soft);text-align:center;padding-top:8px}
.icon{display:inline-block;flex:none}
</style>
</head>
<body>
<svg width="0" height="0" style="position:absolute" aria-hidden="true">
  <defs>
    <symbol id="i-clock" viewBox="0 0 20 20"><circle cx="10" cy="10" r="8.5" fill="#fff" stroke="#777" stroke-width="1.5"/><path d="M10 4v6l4 2" fill="none" stroke="#555" stroke-width="1.5"/></symbol>
    <symbol id="i-pie" viewBox="0 0 20 20"><path d="M10 10V1.5A8.5 8.5 0 0 1 18.5 10z" fill="#d33"/><path d="M10 10h8.5A8.5 8.5 0 0 1 3 15z" fill="#3a7fd5"/><path d="M10 10 3 15A8.5 8.5 0 0 1 10 1.5z" fill="#4bb04b"/></symbol>
    <symbol id="i-size" viewBox="0 0 20 20"><rect x="1" y="2" width="18" height="5" fill="#d55"/><rect x="1" y="8" width="18" height="5" fill="#5b5"/><rect x="1" y="14" width="18" height="5" fill="#57b"/></symbol>
    <symbol id="i-plus" viewBox="0 0 20 20"><path d="M7 1h6v6h6v6h-6v6H7v-6H1V7h6z" fill="#3aa822" stroke="#1f6a10" stroke-width=".8"/></symbol>
    <symbol id="i-tick" viewBox="0 0 20 20"><path d="M2 11l5 5L18 4" fill="none" stroke="var(--tick)" stroke-width="3.4" stroke-linecap="round" stroke-linejoin="round"/></symbol>
    <symbol id="i-note" viewBox="0 0 20 20"><path d="M2 3h16v10H9l-4 4v-4H2z" fill="var(--bubble)"/><path d="M5 6.5h10M5 9.5h8" stroke="#fff" stroke-width="1.2"/></symbol>
    <symbol id="i-list" viewBox="0 0 20 20"><rect x="1" y="2" width="18" height="16" fill="#fff" stroke="#3a7fd5"/><path d="M3 6h2M7 6h10M3 10h2M7 10h10M3 14h2M7 14h10" stroke="#3a7fd5" stroke-width="1.6"/></symbol>
  </defs>
</svg>

<header class="status-bar">
  <span>Tablet</span><span class="clock">10:45 AM</span><span>100%</span>
</header>

<nav class="top-bar">
  <div class="nav-btn" style="left:14px;width:131px">Seating chart</div>
  <div class="nav-btn" style="left:161px;width:93px">Specials</div>
  <div class="nav-btn" style="left:271px;width:118px">Staff notes</div>
  <div class="app-title">Dinewell</div>
  <div class="nav-btn" style="left:919px;width:113px">Calendar</div>
  <div class="nav-btn is-active" style="left:1046px;width:131px">Managment</div>
</nav>

<section class="stats-bar">
  <div class="stat now" style="left:13px;width:190px">2:17 PM, Mon Sep 10</div>
  <div class="stat" style="left:226px;width:151px"><span class="label">Avg Wait Time</span><span>25 mins</span></div>
  <div class="stat" style="left:396px;width:151px"><span class="label">Open Tables</span><span>66</span></div>
  <div class="stat" style="left:564px;width:196px"><span class="label">Checked In</span><span>14 groups - 77 people</span></div>
  <div class="stat" style="left:774px;width:196px"><span class="label">Currently Steated</span><span>11/256</span></div>
  <div class="stat soft" style="left:984px;width:202px"><span class="label">Open Reservation</span><span>370 people</span></div>
</section>

<aside class="wait-list">
  <div class="wait-head"><svg class="icon" width="18" height="18"><use href="#i-list"/></svg>Wait List</div>
  <div class="wait-input">Add a party to the wait list...</div>
  <ul class="wait-rows">
    <li class="wait-row"><div><div class="name">Mara Lane</div><div class="party">party of 3</div></div><div class="since recent">5m (2:02 PM)</div></li>
    <li class="wait-row"><div><div class="name">Mara Lane</div><div class="party">party of 3</div></div><div class="since">5m (2:02 PM)</div></li>
    <li class="wait-row"><div><div class="name">Mara Lane</div><div class="party">party of 3</div></div><div class="since">5m (2:02 PM)</div></li>
    <li class="wait-row"><div><div class="name">Mara Lane</div><div class="party">party of 3</div></div><div class="since">5m (2:02 PM)</div></li>
    <li class="wait-row"><div><div class="name">Mara Lane</div><div class="party">party of 3</div></div><div class="since recent">5m (2:02 PM)</div></li>
    <li class="wait-row"><div><div class="name">Mara Lane</div><div class="party">party of 3</div></div><div class="since">5m (2:02 PM)</div></li>
    <li class="wait-row"><div><div class="name">Mara Lane</div><div class="party">party of 3</div></div><div class="since">5m (2:02 PM)</div></li>
  </ul>
</aside>

<!-- Column one -->
<article class="res-card" style="left:414px;top:188px">
  <div class="card-head"><svg class="icon" width="19" height="19"><use href="#i-clock"/></svg><span class="time">12:00 PM</span><svg class="icon" width="17" height="17"><use href="#i-pie"/></svg><span class="fill">8/24</span><svg class="icon" width="16" height="16"><use href="#i-size"/></svg><span class="size">Size</span><svg class="icon" width="20" height="20"><use href="#i-plus"/></svg></div>
  <div class="card-body">
    <div class="res-row faded"><div class="guest">Mara Lane<div class="note">I would like aboot in the corner</div></div><div class="flags"><svg class="icon" width="18" height="18"><use href="#i-tick"/></svg></div><div class="count">4</div><div class="total">14</div></div>
    <div class="res-row"><div class="guest">Mara Lane<div class="note">birtday party</div></div><div class="flags"><svg class="icon" width="18" height="18"><use href="#i-tick"/></svg></div><div class="count">3</div><div class="total"></div></div>
    <div class="res-row faded"><div class="guest">Mara Lane<div class="note">I would like aboot in the corner</div></div><div class="flags"><svg class="icon" width="18" height="18"><use href="#i-note"/></svg></div><div class="count">2</div><div class="total" style="padding-top:22px">1</div></div>
  </div>
</article>

<article class="res-card" style="left:414px;top:368px">
  <div class="card-head"><svg class="icon" width="19" height="19"><use href="#i-clock"/></svg><span class="time">12:25 PM</span><svg class="icon" width="17" height="17"><use href="#i-pie"/></svg><span class="fill full">FULL</span><svg class="icon" width="16" height="16"><use href="#i-size"/></svg><span class="size">Size</span><svg class="icon" width="20" height="20"><use href="#i-plus"/></svg></div>
  <div class="card-body">
    <div class="res-row faded"><div class="guest">Mara Lane<div class="note">I would like aboot in the corner</div></div><div class="flags"><svg class="icon" width="18" height="18"><use href="#i-tick"/></svg></div><div class="count">4</div><div class="total"></div></div>
    <div class="res-row"><div class="guest">Mara Lane<div class="note">birtday party</div></div><div class="flags"><svg class="icon" width="18" height="18"><use href="#i-note"/></svg><svg class="icon" width="18" height="18"><use href="#i-tick"/></svg></div><div class="count">3</div><div class="total">14</div></div>
    <div class="res-row faded"><div class="guest">Mara Lane<div class="note">I would like aboot in the corner</div></div><div class="flags"><svg class="icon" width="18" height="18"><use href="#i-note"/></svg></div><div class="count">2</div><div class="total" style="padding-top:22px">1</div></div>
  </div>
</article>

<article class="res-card" style="left:414px;top:548px">
  <div class="card-head"><svg class="icon" width="19" height="19"><use href="#i-clock"/></svg><span class="time">15:35 PM</span><svg class="icon" width="17" height="17"><use href="#i-pie"/></svg><span class="fill full">FULL</span><svg class="icon" width="16" height="16"><use href="#i-size"/></svg><span class="size">Size</span><svg class="icon" width="20" height="20"><use href="#i-plus"/></svg></div>
  <div class="card-body">
    <div class="res-row faded"><div class="guest">Mara Lane<div class="note">I would like aboot in the corner</div></div><div class="flags"><svg class="icon" width="18" height="18"><use href="#i-tick"/></svg></div><div class="count">4</div><div class="total"></div></div>
    <div class="res-row"><div class="guest">Mara Lane<div class="note">birtday party</div></div><div class="flags"><svg class="icon" width="18" height="18"><use href="#i-note"/></svg><svg class="icon" width="18" height="18"><use href="#i-tick"/></svg></div><div class="count">3</div><div class="total">14</div></div>
    <div class="res-row faded"><div class="guest">Mara Lane<div class="note">I would like aboot in the corner</div></div><div class="flags"><svg class="icon" width="18" height="18"><use href="#i-note"/></svg></div><div class="count">2</div><div class="total" style="padding-top:22px">1</div></div>
  </div>
</article>

<article class="res-card" style="left:414px;top:730px">
  <div class="card-head"><svg class="icon" width="19" height="19"><use href="#i-clock"/></svg><span class="time">20:00 PM</span><svg class="icon" width="17" height="17"><use href="#i-pie"/></svg><span class="fill full">FULL</span><svg class="icon" width="16" height="16"><use href="#i-size"/></svg><span class="size">Size</span><svg class="icon" width="20" height="20"><use href="#i-plus"/></svg></div>
  <div class="card-body">
    <div class="res-row faded"><div class="guest">Mara Lane<div class="note">I would like aboot in the corner</div></div><div class="flags"><svg class="icon" width="18" height="18"><use href="#i-tick"/></svg></div><div class="count">4</div><div class="total"></div></div>
    <div class="res-row"><div class="guest">Mara Lane<div class="note">birtday party</div></div><div class="flags"><svg class="icon" width="18" height="18"><use href="#i-note"/></svg><svg class="icon" width="18" height="18"><use href="#i-tick"/></svg></div><div class="count">3</div><div class="total">14</div></div>
  </div>
</article>

<!-- Column two -->
<article class="res-card" style="left:812px;top:188px">
  <div class="card-head"><svg class="icon" width="19" height="19"><use href="#i-clock"/></svg><span class="time">12:00 PM</span><svg class="icon" width="17" height="17"><use href="#i-pie"/></svg><span class="fill">8/24</span><svg class="icon" width="16" height="16"><use href="#i-size"/></svg><span class="size">Size</span><svg class="icon" width="20" height="20"><use href="#i-plus"/></svg></div>
  <div class="card-body">
    <div class="res-row faded"><div class="guest">Mara Lane<div class="note">I would like aboot in the corner</div></div><div class="flags"><svg class="icon" width="18" height="18"><use href="#i-tick"/></svg></div><div class="count">4</div><div class="total">14</div></div>
    <div class="res-row"><div class="guest">Mara Lane<div class="note">birtday party</div></div><div class="flags"><svg class="icon" width="18" height="18"><use href="#i-tick"/></svg></div><div class="count">3</div><div class="total"></div></div>
    <div class="res-row faded"><div class="guest">Mara Lane<div class="note">I would like aboot in the corner</div></div><div class="flags"><svg class="icon" width="18" height="18"><use href="#i-note"/></svg></div><div class="count">2</div><div class="total" style="padding-top:22px">1</div></div>
  </div>
</article>

<article class="res-card" style="left:812px;top:367px">
  <div class="card-head"><svg class="icon" width="19" height="19"><use href="#i-clock"/></svg><span class="time">20:00 PM</span><svg class="icon" width="17" height="17"><use href="#i-pie"/></svg><span class="fill full">FULL</span><svg class="icon" width="16" height="16"><use href="#i-size"/></svg><span class="size">Size</span><svg class="icon" width="20" height="20"><use href="#i-plus"/></svg></div>
  <div class="card-body">
    <div class="res-row faded"><div class="guest">Mara Lane<div class="note">I would like aboot in the corner</div></div><div class="flags"><svg class="icon" width="18" height="18"><use href="#i-tick"/></svg></div><div class="count">4</div><div class="total"></div></div>
    <div class="res-row"><div class="guest">Mara Lane<div class="note">birtday party</div></div><div class="flags"><svg class="icon" width="18" height="18"><use href="#i-note"/></svg><svg class="icon" width="18" height="18"><use href="#i-tick"/></svg></div><div class="count">3</div><div class="total">14</div></div>
  </div>
</article>

<article class="res-card" style="left:812px;top:514px">
  <div class="card-head"><svg class="icon" width="19" height="19"><use href="#i-clock"/></svg><span class="time">15:35 PM</span><svg class="icon" width="17" height="17"><use href="#i-pie"/></svg><span class="fill full">FULL</span><svg class="icon" width="16" height="16"><use href="#i-size"/></svg><span class="size">Size</span><svg class="icon" width="20" height="20"><use href="#i-plus"/></svg></div>
  <div class="card-body">
    <div class="res-row faded"><div class="guest">Mara Lane<div class="note">I would like aboot in the corner</div></div><div class="flags"><svg class="icon" width="18" height="18"><use href="#i-tick"/></svg></div><div class="count">4</div><div class="total"></div></div>
    <div class="res-row"><div class="guest">Mara Lane<div class="note">birtday party</div></div><div class="flags"><svg class="icon" width="18" height="18"><use href="#i-note"/></svg><svg class="icon" width="18" height="18"><use href="#i-tick"/></svg></div><div class="count">3</div><div class="total">14</div></div>
    <div class="res-row faded"><div class="guest">Mara Lane<div class="note">I would like aboot in the corner</div></div><div class="flags"><svg class="icon" width="18" height="18"><use href="#i-note"/></svg></div><div class="count">2</div><div class="total" style="padding-top:22px">1</div></div>
  </div>
</article>

<article class="res-card" style="left:812px;top:695px">
  <div class="card-head"><svg class="icon" width="19" height="19"><use href="#i-clock"/></svg><span class="time">12:25 PM</span><svg class="icon" width="17" height="17"><use href="#i-pie"/></svg><span class="fill full">FULL</span><svg class="icon" width="16" height="16"><use href="#i-size"/></svg><span class="size">Size</span><svg class="icon" width="20" height="20"><use href="#i-plus"/></svg></div>
  <div class="card-body">
    <div class="res-row faded"><div class="guest">Mara Lane<div class="note">I would like aboot in the corner</div></div><div class="flags"><svg class="icon" width="18" height="18"><use href="#i-tick"/></svg></div><div class="count">4</div><div class="total"></div></div>
    <div class="res-row"><div class="guest">Mara Lane<div class="note">birtday party</div></div><div class="flags"><svg class="icon" width="18" height="18"><use href="#i-note"/></svg><svg class="icon" width="18" height="18"><use href="#i-tick"/></svg></div><div class="count">3</div><div class="total">14</div></div>
    <div class="res-row faded"><div class="guest">Mara Lane<div class="note">I would like aboot in the corner</div></div><div class="flags"><svg class="icon" width="18" height="18"><use href="#i-note"/></svg></div><div class="count">2</div><div class="total" style="padding-top:22px">1</div></div>
  </div>
</article>
</body>
</html>
```